2024 Comprehensive Needs Assessment

Design our 2024 Binder Report Cover. Front, Spine, Back. We are in the Education field, reporting data for strategic planning. I have attached our color palette and the previous years covers as a sample.

```html
<!DOCTYPE html>
<html lang="en">
<head>
<meta charset="utf-8">
<title>Cedarvale School District – 2024 Comprehensive Needs Assessment Binder Cover</title>
<link rel="stylesheet" href="https://fonts.googleapis.com/css2?family=Bebas+Neue&family=Montserrat:wght@400;600;700&family=Raleway:wght@200;300&display=swap">
<style>
  :root{
    --paper:#ffffff;
    --spine:#41a8c4;
    --ocean:#4489b8;
    --teal-deep:#00808a;
    --berry:#6e3b44;
    --coral:#e8384f;
    --mint:#3bbfb0;
    --copper:#c97b45;
    --leaf:#8db53c;
    --ink:#222222;
  }
  *{margin:0;padding:0;box-sizing:border-box}
  html,body{width:1200px;height:782px;overflow:hidden;background:var(--paper)}
  .cover{position:relative;width:1200px;height:782px;overflow:hidden;background:var(--paper);font-family:"Montserrat",Arial,sans-serif;color:var(--ink)}
  .backdrop{position:absolute;inset:0}
  .accent-bar{position:absolute;height:4px;background:var(--copper);border-radius:2px}
  .brand{position:absolute;display:flex;align-items:center;gap:7px;font-family:"Montserrat",Arial,sans-serif;font-weight:600;color:var(--ink);line-height:1.1}
  .brand-dot{width:14px;height:14px;border-radius:50%;background:var(--leaf);flex:none}
  .brand-back{left:188px;top:158px;font-size:16px}
  .brand-front{left:694px;top:76px;font-size:16px}
  .back-intro{position:absolute;left:198px;top:243px;width:250px;font-size:9.5px;line-height:15px;color:var(--ink)}
  .contact{position:absolute;left:196px;top:560px;font-size:9.5px;color:var(--paper);line-height:13px}
  .contact dt{font-weight:700;color:var(--copper)}
  .contact dt.mail{color:var(--leaf)}
  .contact dd{margin-bottom:21px}
  .spine{position:absolute;left:568px;top:0;width:80px;height:782px;background:var(--spine)}
  .spine-run{position:absolute;left:-351px;top:351px;width:782px;height:80px;transform:rotate(-90deg);color:var(--paper)}
  .spine-run > *{position:absolute;white-space:nowrap}
  .spine-name{left:527px;top:16px;font-family:"Bebas Neue",Impact,sans-serif;font-size:42px;line-height:36px;letter-spacing:1px}
  .spine-district{left:529px;top:52px;font-family:"Montserrat",Arial,sans-serif;font-size:8.5px;letter-spacing:4.3px}
  .spine-year{left:377px;top:16px;font-family:"Raleway",Arial,sans-serif;font-weight:200;font-size:50px;line-height:46px}
  .spine-report{left:217px;top:20px;font-family:"Bebas Neue",Impact,sans-serif;font-size:19px;line-height:17px}
  .spine-report b{font-weight:400;display:block;font-size:22px;line-height:20px}
  .spine-brand{left:36px;top:22px;font-family:"Montserrat",Arial,sans-serif;font-weight:700;font-size:14px;line-height:16px;display:flex;align-items:center;gap:6px}
  .spine-brand .brand-dot{background:var(--paper);width:11px;height:11px}
  .front-title{position:absolute;left:854px;top:262px;color:var(--paper)}
  .front-name{font-family:"Bebas Neue",Impact,sans-serif;font-size:78px;line-height:68px;letter-spacing:2px}
  .front-district{font-family:"Montserrat",Arial,sans-serif;font-size:19px;letter-spacing:8.6px;font-weight:400;margin-top:-2px}
  .front-year{position:absolute;left:906px;top:352px;font-family:"Raleway",Arial,sans-serif;font-weight:200;font-size:104px;line-height:100px;color:var(--mint);letter-spacing:-1px}
</style>
</head>
<body>
<main class="cover">
  <svg class="backdrop" width="1200" height="782" viewBox="0 0 1200 782" aria-hidden="false">
    <defs>
      <clipPath id="lower-half"><rect x="0" y="440" width="1200" height="342"/></clipPath>
      <radialGradient id="sketch-tone" cx="50%" cy="45%" r="55%">
        <stop offset="0" stop-color="#f4f4f4"/>
        <stop offset="0.8" stop-color="#e6e6e6"/>
        <stop offset="1" stop-color="#cfcfcf"/>
      </radialGradient>
      <linearGradient id="blocks-tone" x1="0" y1="0" x2="1" y2="1">
        <stop offset="0" stop-color="#5a9fd0"/>
        <stop offset="0.6" stop-color="#e9eef4"/>
        <stop offset="1" stop-color="#9aa35a"/>
      </linearGradient>
    </defs>
    <path class="ocean-sweep" fill="var(--ocean)" d="M0,495 C250,432 560,418 770,468 C960,515 1100,610 1200,690 L1200,782 L0,782 Z"/>
    <circle class="teal-ring" cx="648" cy="402" r="313" fill="var(--teal-deep)" clip-path="url(#lower-half)"/>
    <circle class="berry-disc" cx="960" cy="395" r="262" fill="var(--berry)"/>
    <circle class="coral-disc" cx="1092" cy="392" r="252" fill="var(--coral)"/>
    <circle class="coral-notch" cx="1058" cy="135" r="96" fill="var(--paper)"/>
    <circle class="copper-ring" cx="1037" cy="147" r="20" fill="none" stroke="var(--copper)" stroke-width="2.5"/>
    <circle class="sketch-window" cx="650" cy="420" r="213" fill="url(#sketch-tone)" role="img" aria-label="Hand-drawn business planning sketch with light bulb, arrows, city skyline and charts"/>
    <path class="data-blocks" fill="url(#blocks-tone)" opacity="0.9" role="img" aria-label="Isometric illustration of stacked blocks with pie chart, wifi sign and laptop"
      d="M912,460 L965,460 L1000,520 L1000,620 L1060,650 L1060,720 L1010,742 L900,700 L800,665 L820,620 L820,570 L880,545 L912,515 Z"/>
  </svg>

  <span class="accent-bar" style="left:123px;top:34px;width:46px"></span>
  <div class="brand brand-back"><span class="brand-dot"></span><span>Learnwell<br>Partners, LLC</span></div>
  <span class="accent-bar" style="left:196px;top:217px;width:53px"></span>
  <p class="back-intro">Lorem ipsum dolor amet consectetur adipiscing elit sed do eiusmod tempor incididunt tulabore dolore magna aliqua. thuis ipsum suspendisse ultrices commodo viverra.</p>
  <span class="accent-bar" style="left:196px;top:517px;width:46px"></span>
  <dl class="contact">
    <dt>Phone:</dt><dd>555-010-4821</dd>
    <dt class="mail">Mail:</dt><dd>info@learnwellpartners.example</dd>
    <dt>Address:</dt><dd style="margin-bottom:0">1200 Orchard Lane<br>Fairview, MS 38000</dd>
  </dl>

  <aside class="spine">
    <div class="spine-run">
      <span class="spine-brand"><span class="brand-dot"></span><span>Learnwell<br>Partners</span></span>
      <span class="spine-report">Comprehensive<b>Needs Assessment</b></span>
      <span class="spine-year">2024</span>
      <span class="spine-name">Cedarvale</span>
      <span class="spine-district">SCHOOL DISTRICT</span>
    </div>
  </aside>

  <div class="brand brand-front"><span class="brand-dot"></span><span>Learnwell<br>Partners, LLC</span></div>
  <header class="front-title">
    <h1 class="front-name">CEDARVALE</h1>
    <p class="front-district">SCHOOL DISTRICT</p>
  </header>
  <p class="front-year">2024</p>
</main>
</body>
</html>
```